Lentil and Vegetable Soup (Sambar) Product Label Design

Sambar is the product and we need a label for that. The label size is 4"x3.33". Attached is the sample label containing all the necessary info.
Mainly show the images of the coconut, onions, chayotes, big egg plant and the lentils (Toor dal). Various design choices are encouraged. This includes various types of fonts, colors, backgrounds, etc.

```html
<!DOCTYPE html>
<html lang="en">
<head>
<meta charset="utf-8">
<title>Samber Spicy Lentil Soup Label</title>
<link href="https://fonts.googleapis.com/css2?family=Libre+Baskerville:wght@400;700&family=Pacifico&family=Lato:wght@400;700&display=swap" rel="stylesheet">
<style>
  :root {
    --stage: #e4e4e4;
    --label-white: #ffffff;
    --sun-yellow: #f9d423;
    --deep-orange: #f39c12;
    --brand-red: #d3202a;
    --soup-orange: #e8731f;
    --text-dark: #3a2a10;
    --leaf-green: #3fae49;
    --brand-purple: #6b3fa0;
  }
  * { margin: 0; padding: 0; box-sizing: border-box; }
  html, body { width: 831px; height: 1200px; overflow: hidden; }
  body {
    background: var(--stage);
    font-family: "Lato", sans-serif;
    color: var(--text-dark);
    position: relative;
  }
  .label {
    position: absolute;
    left: 36px; top: 250px;
    width: 760px; height: 700px;
    background: linear-gradient(180deg, var(--sun-yellow) 0%, var(--deep-orange) 100%);
    overflow: hidden;
  }
  .side-panel {
    position: absolute; top: 0; height: 540px; width: 175px;
    padding: 40px 16px;
    font-size: 13px; line-height: 1.55;
  }
  .side-panel.left { left: 0; }
  .side-panel.right { right: 0; text-align: right; }
  .ingredients b { display: block; font-size: 14px; margin-bottom: 4px; }
  .claims { margin-top: 60px; font-weight: 700; font-size: 13px; letter-spacing: .5px; }
  .claims .green { color: #1f7a2c; }
  .claims .red { color: var(--brand-red); }
  .badge {
    width: 70px; height: 70px; border-radius: 50%;
    background: var(--leaf-green);
    margin: 160px 0 18px auto;
  }
  .brand-dot {
    width: 40px; height: 40px; border-radius: 50%;
    background: var(--brand-purple); margin-left: auto; margin-bottom: 40px;
  }
  .front-panel {
    position: absolute; left: 175px; top: 0;
    width: 410px; height: 540px;
    background: var(--label-white);
    text-align: center;
    padding-top: 40px;
  }
  .product-name {
    font-family: "Libre Baskerville", serif;
    font-weight: 700; font-size: 40px; letter-spacing: 2px;
    color: var(--brand-red);
  }
  .product-type {
    font-family: "Pacifico", cursive;
    font-size: 34px; color: var(--brand-red);
    margin-top: 2px;
  }
  .soup-photo {
    display: block; margin: 14px auto 0;
    width: 300px; height: 160px;
  }
  .veg-photo {
    display: block; margin: 6px auto 0;
    width: 330px; height: 120px;
  }
  .special {
    position: absolute; left: 0; right: 0; bottom: 0;
    height: 52px; line-height: 52px;
    background: var(--sun-yellow);
    font-family: "Libre Baskerville", serif;
    font-weight: 700; font-size: 20px; color: var(--text-dark);
  }
  .footer-band {
    position: absolute; left: 0; right: 0; top: 540px; bottom: 0;
    background: var(--label-white);
    border-top: 4px solid var(--text-dark);
  }
  .footer-note {
    position: absolute; left: 16px; top: 18px; width: 150px;
    font-size: 11px; line-height: 1.4;
  }
  .brand-name {
    position: absolute; left: 0; right: 0; top: 48px;
    text-align: center;
    font-family: "Pacifico", cursive;
    font-size: 40px; color: var(--brand-purple);
  }
  .footer-origin {
    position: absolute; right: 16px; top: 18px;
    font-size: 11px; text-align: right;
  }
</style>
</head>
<body>
  <div class="label">
    <aside class="side-panel left">
      <p class="ingredients"><b>Ingredients:</b>Toor dal, tamarind, onion, coconut, coriander, turmeric, mustard seeds, red chilli, curry leaves, salt.</p>
      <p class="claims"><span class="green">NO PRESERVATIVES</span><br><span class="red">NO ADDITIVE</span></p>
    </aside>

    <section class="front-panel">
      <h1 class="product-name">SAMBER</h1>
      <h2 class="product-type">Spicy Lentil Soup</h2>
      <svg class="soup-photo" viewBox="0 0 300 160" role="img" aria-label="Bowl of orange lentil soup garnished with coriander and cream">
        <defs>
          <radialGradient id="soupTone" cx="50%" cy="45%" r="60%">
            <stop offset="0%" stop-color="#f39a3c"/>
            <stop offset="100%" stop-color="#d9621a"/>
          </radialGradient>
        </defs>
        <ellipse cx="150" cy="80" rx="148" ry="76" fill="url(#soupTone)"/>
      </svg>
      <svg class="veg-photo" viewBox="0 0 330 120" role="img" aria-label="Onions, eggplant, chayote and a halved coconut with leaves">
        <defs>
          <linearGradient id="vegTone" x1="0" x2="1" y1="0" y2="0">
            <stop offset="0%" stop-color="#b8406a"/>
            <stop offset="45%" stop-color="#7fae4a"/>
            <stop offset="100%" stop-color="#8a5a36"/>
          </linearGradient>
        </defs>
        <rect x="0" y="10" width="330" height="100" rx="50" fill="url(#vegTone)" opacity="0.85"/>
      </svg>
      <div class="special">COCONUT &amp; ONION SPECIAL</div>
    </section>

    <aside class="side-panel right">
      <div class="badge"></div>
      <div class="brand-dot"></div>
      <p>Net Wt. 300 g<br>Best before 6 months</p>
    </aside>

    <footer class="footer-band">
      <p class="footer-note">Serve hot with rice or idli. Store in a cool, dry place.</p>
      <p class="brand-name">Tharavu</p>
      <p class="footer-origin">Made in India</p>
    </footer>
  </div>
</body>
</html>
```